Rocket business card

Modern business card design, use of color is good with clean space too.

Things to include on card:

Quote: I add fuel to your optometry practice

- Eyewear Sales
- Admin Duties
- Revenue Collection
- Leadership
- Tech Adoption
- COGS Reduction
- Product Sourcing
-Medical Growth

Dalton Vessey, CEO
Glint Harbor
Text Me! 847-302-1964
dalton@glintharbor.example

```html
<!DOCTYPE html>
<html lang="en">
<head>
<meta charset="utf-8">
<title>Glint Harbor – Business Card</title>
<link href="https://fonts.googleapis.com/css2?family=Open+Sans:wght@400;600;700;800&display=swap" rel="stylesheet">
<style>
  :root {
    --stage: #e9e6e2;
    --card-white: #f7f7f7;
    --card-black: #000000;
    --ink: #111111;
    --orange: #e96335;
    --divider: #3a3a3a;
    --service-grey: #bdbdbd;
    --white: #ffffff;
  }
  * { box-sizing: border-box; margin: 0; padding: 0; }
  html, body {
    width: 1200px; height: 900px; overflow: hidden;
    background: var(--stage);
    font-family: "Open Sans", Arial, sans-serif;
  }
  .stage {
    width: 1200px; height: 900px;
    display: flex; flex-direction: column; align-items: center; justify-content: center;
    gap: 40px;
  }
  .card {
    position: relative; width: 660px; height: 377px; overflow: hidden;
    box-shadow: 0 6px 18px rgba(0,0,0,0.18);
  }

  /* ---------- back side ---------- */
  .card--back { background: var(--card-black); color: var(--white); }
  .brand--back {
    position: absolute; left: 0; right: 0; top: 92px;
    display: flex; align-items: center; justify-content: center; gap: 16px;
  }
  .brand-dot {
    width: 46px; height: 46px; border-radius: 50%;
  }
  .brand--back .brand-dot { background: var(--white); }
  .brand-name {
    font-weight: 400; letter-spacing: 3px; text-transform: uppercase; white-space: nowrap;
  }
  .brand--back .brand-name { font-size: 44px; color: var(--white); }
  .services {
    position: absolute; display: grid; grid-template-columns: auto auto;
    column-gap: 26px; row-gap: 2px;
    list-style: none; font-size: 14px; color: var(--service-grey);
  }
  .services--left { left: 70px; bottom: 62px; }
  .services--right { right: 60px; top: 196px; }
  .services li::before { content: "- "; }

  /* ---------- front side ---------- */
  .card--front { background: var(--card-white); color: var(--ink); }
  .brand--front {
    position: absolute; left: 40px; top: 110px; width: 250px;
    display: flex; flex-direction: column; align-items: center; gap: 14px;
  }
  .brand--front .brand-dot { background: var(--orange); width: 58px; height: 58px; }
  .brand--front .brand-name { font-size: 30px; color: var(--ink); letter-spacing: 2px; }
  .divider {
    position: absolute; left: 318px; top: 60px; width: 1.5px; height: 176px;
    background: var(--divider);
  }
  .person { position: absolute; left: 346px; top: 62px; }
  .person-name { font-size: 30px; font-weight: 800; color: var(--orange); line-height: 1; letter-spacing: 0.5px; }
  .person-role { font-size: 16px; font-weight: 400; line-height: 1.2; }
  .contact {
    position: absolute; left: 340px; top: 168px; list-style: none;
    font-size: 17px; letter-spacing: 0.5px;
  }
  .contact li { display: flex; align-items: center; gap: 12px; height: 30px; }
  .contact svg { width: 20px; height: 20px; flex: none; }
  .wave { position: absolute; left: 0; bottom: 0; width: 660px; height: 150px; }
</style>
</head>
<body>
<main class="stage">

  <section class="card card--back" aria-label="Card back">
    <div class="brand brand--back">
      <span class="brand-dot"></span>
      <span class="brand-name">Glint Harbor</span>
    </div>
    <ul class="services services--right">
      <li>Tech Adoption</li>
      <li>COGS Reduction</li>
      <li>Product Sourcing</li>
      <li>Medical Growth</li>
    </ul>
    <ul class="services services--left">
      <li>Eyewear Sales</li>
      <li>Admin Duties</li>
      <li>Revenue Collection</li>
      <li>Leadership</li>
    </ul>
  </section>

  <section class="card card--front" aria-label="Card front">
    <div class="brand brand--front">
      <span class="brand-dot"></span>
      <span class="brand-name">Glint Harbor</span>
    </div>
    <span class="divider"></span>
    <div class="person">
      <p class="person-name">Dalton Vessey</p>
      <p class="person-role">CEO</p>
    </div>
    <ul class="contact">
      <li>
        <svg viewBox="0 0 24 24" aria-hidden="true"><path d="M6 3c-2 1-3 3-2 6 2 6 6 10 12 12 3 1 5 0 6-2l-3-3-3 2c-3-1-6-4-7-7l2-3z" fill="none" stroke="var(--orange)" stroke-width="2" stroke-linejoin="round"/></svg>
        <span>847-302-1964</span>
      </li>
      <li>
        <svg viewBox="0 0 24 24" aria-hidden="true"><rect x="2" y="5" width="20" height="14" fill="none" stroke="var(--orange)" stroke-width="2.4"/><path d="M2 5l10 8 10-8" fill="none" stroke="var(--orange)" stroke-width="2.4"/></svg>
        <span>dalton@glintharbor.example</span>
      </li>
    </ul>
    <svg class="wave" viewBox="0 0 660 150" preserveAspectRatio="none" aria-hidden="true">
      <path d="M0 14 C 140 0, 260 20, 390 62 C 430 75, 460 80, 480 82 C 440 80, 400 70, 360 60 C 240 30, 120 14, 0 24 Z" fill="var(--orange)"/>
      <path d="M0 36 C 150 22, 290 60, 420 98 C 520 122, 600 112, 660 100 L 660 150 L 0 150 Z" fill="var(--orange)"/>
    </svg>
  </section>

</main>
</body>
</html>
```